Wine Label Design-Marrowgate Vineyard

Marrowgate Vineyard is in the Barossa Valley in South Australia. The Barossa is recognized as Australia's premier wine region, producing Australia's icon wines and some " new takes on traditional".
This family owned and operated vineyard grows some exceptionally high quality fruit. Most of the fruit is sold and used for some of Australia's most iconic wines. Small quantities are retained by the owners for some wines with very limited availability. (Wines were previously sold as BrellMarston Vineyards Marrowgate ( Shiraz, Cabernet etc).

The wines will in the future be labeled simply ‘Marrowgate Vineyard’. The label will launch this new identity for the single family single vineyard and its high quality wines which are a true expression of the vineyard and derive from the Marrowgate common to this ancient area (800-2000 million years old).
The label should reflect
• Single vineyard, family owned
• vines in very old rock & soils
• High quality & reliability
• Edgy but true, design based thinking (Please note:blue is generally seen as an unacceptable colour for a wine label?? Don’t ask me why)

The wines will be sold mostly direct in Australia ( ie not through retail stores), with limited export to Asia, Scandinavia and Canada.
There are three quality levels and price points in the portfolio
1. Entry level premium for everyday drinking for discriminating drinkers-approx AUD20
2. Super Premium-approx AUD30
3. Limited Release ultlra premium-AUD75-90?
We envisage three variations on the label but with an obvious & common design element. This design element should be able to be used for corporate identification and promotion
The paper stock will be waterproof and self adhesive. Our preference is for designs that engage the user by appealing to both sight and touch. It is preferred that textures be added eg embossing, high build varnish etc-rather than be a facet of the stock itself.
For information on statutory label requirements refer to www.vinoregistry-example.com . In brief
o Front label need not show any mandatory information. However we would prefer Variety, Barossa Valley, Year and alcohol to be shown on the front label
o Back label should show all mandatories and allow for a bar code

Reason: I've had a problem with my wireless broadband account and reception has been intermittent to say the least to the extent that I switched off at the weekend. Just going downtown now for a 'polite discussion' with my service provider.

Reason: I have receiver insufficient designs of quality which we would consider. Too many designs have a "cut and paste" appearance - too few exhibit an original art/design element which truly identifies the product.

Gals & Guys

most of the designs submitted lack punch and originality and are totally unmemorable.
Please-get on Zindle or whatever enter "Wine Label Designs" and do some research b4 u waste your time and mine. Formulaic cut and paste will not win the day. That's not to say that cut and paste can't work-but it must have some originality, impact and command attention. Please surprise me.

Following on from a question from a designer about who is our competition and what we are looking for I sent the following 
"I don't think I can add anything new. Read the brief and comments again and research wine labels on the web. In 30 minutes you'll get a good idea of the creative edgy designs in the industry. There are a plethora of collections. Our competition-anyone with a label. In 2010 there were over 2400 "producers" in other words 2400 producers with at least one label. In fact there are over 25000 Australian wines and then the numerous imported wines.

Target Market(s)

$20 people who budget everyday but have graduated from drinking 'entry level' wines. These people will likely fit into Cat. (b) in the $30 wine

$30 (a) will not over-compromise on some everyday discretionary expenditure.(b) might buy for special occasions

$70-$90 Professional/successful people with high disposable/discretionary income not particularly worried about recession. wine geeks.

Industry/Entity Type

Retail

Requirements
Must have
• identifiable element across range of wines

```html
<!DOCTYPE html>
<html lang="en">
<head>
<meta charset="utf-8">
<title>Marrowgate Vineyard – Label Range</title>
<link rel="stylesheet" href="https://fonts.googleapis.com/css2?family=Libre+Baskerville&family=Playfair+Display:ital@1&family=Arimo:wght@700&display=swap">
<style>
  :root {
    --canvas: #ececec;
    --paper: #ffffff;
    --ink: #111111;
    --vintage-red: #9c1b2b;
    --band-viognier: #7e9a2c;
    --band-cabernet: #23317a;
    --band-blend: #12163a;
    --band-shiraz: #a3182f;
    --band-text: #ffffff;
  }
  * { box-sizing: border-box; margin: 0; padding: 0; }
  html, body { width: 1200px; height: 900px; overflow: hidden; }
  body {
    background: var(--canvas);
    display: flex;
    align-items: center;
    justify-content: center;
  }
  .label-range {
    display: flex;
    gap: 40px;
  }
  .label {
    width: 230px;
    height: 284px;
    background: var(--paper);
    padding: 8px;
    box-shadow: 0 1px 3px rgba(0,0,0,0.12);
  }
  .label__frame {
    height: 100%;
    border: 1.5px solid var(--ink);
    display: flex;
    flex-direction: column;
    align-items: center;
    padding-top: 20px;
  }
  .brand-mark {
    width: 46px;
    height: 46px;
    background: var(--ink);
    margin-bottom: 24px;
  }
  .brand-name {
    font-family: "Libre Baskerville", serif;
    color: var(--ink);
    text-align: center;
    text-transform: uppercase;
    line-height: 1.05;
    font-weight: 400;
  }
  .brand-name__main { display: block; font-size: 19px; letter-spacing: 0.2px; }
  .brand-name__sub { display: block; font-size: 13px; }
  .vintage {
    display: flex;
    align-items: center;
    gap: 5px;
    margin-top: 12px;
    font-family: "Libre Baskerville", serif;
    font-size: 13px;
    line-height: 1.1;
    color: var(--vintage-red);
  }
  .vintage__rule {
    width: 24px;
    height: 1px;
    background: var(--ink);
  }
  .region {
    font-family: "Arimo", sans-serif;
    font-weight: 700;
    font-size: 8.5px;
    letter-spacing: 0.3px;
    color: var(--ink);
    margin-top: 4px;
  }
  .variety-band {
    align-self: stretch;
    margin-top: 12px;
    height: 44px;
    padding-left: 22px;
    color: var(--band-text);
    display: flex;
    flex-direction: column;
    justify-content: center;
  }
  .variety-band__name {
    font-family: "Playfair Display", serif;
    font-style: italic;
    font-size: 20px;
    line-height: 1;
  }
  .variety-band__state {
    font-family: "Arimo", sans-serif;
    font-weight: 700;
    font-size: 5.5px;
    letter-spacing: 0.3px;
    margin-top: 3px;
  }
  .label--viognier .variety-band { background: var(--band-viognier); }
  .label--cabernet .variety-band { background: var(--band-cabernet); }
  .label--blend .variety-band { background: var(--band-blend); }
  .label--shiraz .variety-band { background: var(--band-shiraz); }
  .bottle-facts {
    margin-top: 10px;
    font-family: "Arimo", sans-serif;
    font-weight: 700;
    font-size: 6.5px;
    line-height: 1.3;
    color: var(--ink);
    text-align: center;
  }
</style>
</head>
<body>
  <main class="label-range">
    <article class="label label--viognier">
      <div class="label__frame">
        <div class="brand-mark"></div>
        <h2 class="brand-name"><span class="brand-name__main">Marrowgate</span><span class="brand-name__sub">Vineyard</span></h2>
        <p class="vintage"><span class="vintage__rule"></span>2012<span class="vintage__rule"></span></p>
        <p class="region">BAROSSA VALLEY</p>
        <div class="variety-band"><span class="variety-band__name">Viognier</span><span class="variety-band__state">SOUTH AUSTRALIA</span></div>
        <p class="bottle-facts">13%Vol<br>750 ml</p>
      </div>
    </article>
    <article class="label label--cabernet">
      <div class="label__frame">
        <div class="brand-mark"></div>
        <h2 class="brand-name"><span class="brand-name__main">Marrowgate</span><span class="brand-name__sub">Vineyard</span></h2>
        <p class="vintage"><span class="vintage__rule"></span>2012<span class="vintage__rule"></span></p>
        <p class="region">BAROSSA VALLEY</p>
        <div class="variety-band"><span class="variety-band__name">Cabernet</span><span class="variety-band__state">SOUTH AUSTRALIA</span></div>
        <p class="bottle-facts">13%Vol<br>750 ml</p>
      </div>
    </article>
    <article class="label label--blend">
      <div class="label__frame">
        <div class="brand-mark"></div>
        <h2 class="brand-name"><span class="brand-name__main">Marrowgate</span><span class="brand-name__sub">Vineyard</span></h2>
        <p class="vintage"><span class="vintage__rule"></span>2012<span class="vintage__rule"></span></p>
        <p class="region">BAROSSA VALLEY</p>
        <div class="variety-band"><span class="variety-band__name">Long Table</span><span class="variety-band__state">SOUTH AUSTRALIA</span></div>
        <p class="bottle-facts">13%Vol<br>750 ml</p>
      </div>
    </article>
    <article class="label label--shiraz">
      <div class="label__frame">
        <div class="brand-mark"></div>
        <h2 class="brand-name"><span class="brand-name__main">Marrowgate</span><span class="brand-name__sub">Vineyard</span></h2>
        <p class="vintage"><span class="vintage__rule"></span>2012<span class="vintage__rule"></span></p>
        <p class="region">BAROSSA VALLEY</p>
        <div class="variety-band"><span class="variety-band__name">Shiraz</span><span class="variety-band__state">SOUTH AUSTRALIA</span></div>
        <p class="bottle-facts">13%Vol<br>750 ml</p>
      </div>
    </article>
  </main>
</body>
</html>
```